Wordpress Website design partner needed for an Arabic Language Institute for English Speakers

We are an online Arabic Language institute, targeting English Speakers around the world and we provide online courses and private group and one on one classes
We are looking for a total of 5 pages designed.
The Design should be mobile-first, and then provide PC for any differences.
I am looking for a consistent design with a lot of white space and in line with our Logo colours.
Images used should be around the theme of Arabic Language/Islamic in Nature, so please do not use any illustrations or images of animals or human beings except for silhouettes or images without faces visible, such as someone facing other way or below torso or hands etc.
The website will eventually be prepared for Wordpress using Divi.
I will provide a very structured outline of what elements and modules each page should have. Therefore I am looking for someone that has an eye for detail and is precise in executing requirements.
I decided to post on this site because I am looking for a long-term partner that can take care of any of our design needs as they come up.
More details to follow
I will do abit more research tomorrow to suggest sample sites
Updates
Gathering more feedback
Target Market(s)
English speakers that want to learn Arabic for Religous purposes such as understanding the Quran
Industry/Entity Type
Education
Colors
Designer to choose colors to be used in the design.
Requirements
Must have
- Mobile First, and design for PC for changes
- Consistency
- Plenty of White Space
- Colour Palette based on Logo
- Colour and Transparent/White Header for when scrolling
- Big Call to Action buttons with contrasting colors
- A consistent footer for all pages with
- -Social Media Icons
- -Contact us
- -Sitemap
- -Copyright
- -Logo
- Anything with a hashtag (#) beforehand in the Doc file means it should be a module like the modules used in Divi Theme, Please check the following website for an explanation of what each module consists of and some examples of it in use. https://www.plumeworkgallery.com/block-parts-guide/
Nice to have
- Parallax Effect
Should not have
- illustrations or images of animals or human beings except for silhouettes or images without faces visible, such as someone facing other way or below torso or hands etc.

```html
<!DOCTYPE html>
<html lang="en">
<head>
<meta charset="utf-8">
<title>QALAM Arabic Academy</title>
<link rel="stylesheet" href="https://fonts.googleapis.com/css2?family=Montserrat:ital,wght@0,400;0,500;0,600;0,700;1,400;1,500&display=swap">
<style>
:root{
  --blue:#1a6db0;
  --blue-dark:#0f4f8a;
  --teal:#1fa3c4;
  --navy:#0b2f55;
  --ink:#222;
  --muted:#6a6a6a;
  --line:#d9dde2;
  --white:#fff;
}
*{box-sizing:border-box;margin:0;padding:0}
html,body{width:1200px;height:3494px;overflow:hidden;background:var(--white);font-family:'Montserrat',sans-serif;color:var(--ink)}
.page{position:relative;width:1200px;height:3494px;overflow:hidden}
.abs{position:absolute}
.btn{position:absolute;display:flex;align-items:center;justify-content:center;color:var(--white);font-weight:700;font-size:11px;letter-spacing:.3px;border-radius:5px;background:linear-gradient(180deg,var(--teal),var(--blue-dark));text-transform:uppercase}
.section-title{position:absolute;left:0;width:1200px;text-align:center;font-weight:600;font-size:28px;color:var(--ink)}
.rule{position:absolute;height:3px;width:30px;background:var(--blue-dark)}

/* top bar */
.topbar{left:0;top:0;width:1200px;height:38px;background:linear-gradient(90deg,var(--blue-dark),var(--teal))}
.topbar .phone{left:172px;top:12px;color:#fff;font-size:11px;font-weight:500;display:flex;gap:5px;align-items:center}
.social{display:flex;gap:9px}
.social span{width:17px;height:17px;border-radius:50%;background:#fff;display:block}
.topbar .social{position:absolute;left:927px;top:10px}

/* header */
.header{left:0;top:38px;width:1200px;height:136px;background:#fff;border-bottom:1px solid #eee}
.brand{position:absolute;display:flex;align-items:center;gap:8px;font-weight:700;color:var(--blue)}
.brand i{display:block;border-radius:50%;background:var(--blue)}
.nav{left:407px;top:62px;display:flex;gap:37px;font-size:14px;font-weight:500;color:#333}
.nav .active{border-bottom:2px solid var(--blue);padding-bottom:4px}

/* hero */
.hero{left:0;top:174px;width:1200px;height:567px;background:radial-gradient(ellipse at 55% 55%,#c99a55 0%,#9b6a2e 45%,#4a2a10 100%)}
.hero h1{position:absolute;left:0;top:193px;width:1200px;text-align:center;color:#fff;font-size:30px;font-weight:600}
.hero p{position:absolute;left:0;top:233px;width:1200px;text-align:center;color:#fff;font-size:15px;line-height:22.5px;font-weight:500}
.arrow{position:absolute;top:268px;width:33px;height:33px;background:#fff;border-radius:3px;display:flex;align-items:center;justify-content:center}

/* about */
.about-text{position:absolute;top:852px;width:272px;font-size:11.5px;line-height:19.5px;color:var(--muted);text-align:justify}
.about-mark{left:470px;top:843px;width:260px;height:257px;display:flex;flex-direction:column;align-items:center;justify-content:center;gap:14px}
.about-mark i{width:150px;height:150px;border-radius:50%;background:linear-gradient(135deg,var(--teal),var(--blue-dark));display:block}
.about-mark b{font-size:30px;font-weight:700;color:var(--blue)}

.card{position:absolute;top:1132px;width:363px;height:260px;border-radius:5px;overflow:hidden}
.card h3{position:absolute;left:0;top:150px;width:100%;text-align:center;color:#fff;font-size:19px;font-weight:600}
.card p{position:absolute;left:36px;top:180px;width:291px;text-align:center;color:#fff;font-size:11.5px;line-height:20px}

/* video */
.video{left:161px;top:1490px;width:878px;height:336px;border-radius:12px;background:linear-gradient(135deg,#c9bba0,#8f7b5c 60%,#6d5a40)}

/* testimonial */
.quote{left:0;top:1944px;width:1200px;text-align:center;font-style:italic;font-size:12.5px;line-height:22px;color:#555}
.dots{left:576px;top:2076px;display:flex;gap:7px}
.dots span{width:12px;height:12px;border:1.5px solid #333;border-radius:50%;display:block}
.dots .on{border-color:var(--teal)}

/* why */
.why{left:0;top:2146px;width:1200px;height:565px;overflow:hidden;background:linear-gradient(180deg,#c8d6e2 0%,#e9eef2 50%,#f4f6f8 100%)}
.why h2{position:absolute;left:662px;top:124px;color:#fff;font-size:28px;font-weight:600}
.why p{position:absolute;left:662px;width:380px;color:#fff;font-size:11.5px;line-height:19.5px}
.btn-white{position:absolute;left:664px;top:402px;width:124px;height:36px;background:#fff;border-radius:5px;color:var(--blue);font-size:11px;font-weight:700;display:flex;align-items:center;justify-content:center}

/* contact */
.contact h2{position:absolute;left:245px;top:2790px;font-size:28px;font-weight:600}
.field{position:absolute;left:612px;width:343px;border:1px solid var(--line);border-radius:4px;font-size:11px;color:#888;padding:12px 18px}

/* subscribe + footer */
.footer{left:0;top:3142px;width:1200px;height:311px;background:linear-gradient(180deg,#0c2a4a,#123a5e 60%,#0b2542)}
.subscribe{left:236px;top:3096px;width:728px;height:76px;background:#fff;border-radius:4px;box-shadow:0 4px 14px rgba(0,0,0,.15)}
.fcol h4{color:#fff;font-size:17px;font-weight:600;margin-bottom:8px}
.fcol li{list-style:none;color:#fff;font-size:11px;line-height:34.5px}
.bottombar{left:0;top:3453px;width:1200px;height:41px;background:linear-gradient(90deg,var(--blue-dark),var(--teal));color:#fff;font-size:11px;font-weight:600;display:flex;align-items:center;justify-content:center}
</style>
</head>
<body>
<div class="page">

  <!-- top bar -->
  <div class="abs topbar">
    <div class="abs phone">
      <svg width="11" height="11" viewBox="0 0 24 24"><path fill="#fff" d="M6.6 10.8a15 15 0 0 0 6.6 6.6l2.2-2.2c.3-.3.7-.4 1-.2 1.1.4 2.3.6 3.6.6.6 0 1 .4 1 1V20c0 .6-.4 1-1 1A17 17 0 0 1 3 4c0-.6.4-1 1-1h3.5c.6 0 1 .4 1 1 0 1.3.2 2.5.6 3.6.1.3 0 .7-.2 1z"/></svg>
      (555) 201-3390
    </div>
    <div class="social"><span></span><span></span><span></span><span></span></div>
  </div>

  <!-- header -->
  <header class="abs header">
    <div class="brand" style="left:171px;top:46px;font-size:22px"><i style="width:22px;height:22px"></i>QALAM</div>
    <nav class="abs nav">
      <span class="active">Home</span><span>About Us</span><span>Courses</span><span>FAQ's</span><span>Contact Us</span>
    </nav>
    <svg class="abs" style="left:863px;top:64px" width="13" height="13" viewBox="0 0 24 24"><circle cx="10" cy="10" r="7" fill="none" stroke="#333" stroke-width="3"/><path d="M15 15l7 7" stroke="#333" stroke-width="3"/></svg>
    <div class="btn" style="left:903px;top:54px;width:125px;height:36px">Book Your Spot</div>
  </header>

  <!-- hero -->
  <section class="abs hero" role="img" aria-label="Open Arabic book with prayer beads in warm light">
    <h1>The Arabic Language Academy</h1>
    <p>Which heps inderstand Allah's words<br>an the Noble Prophets teachings directly<br>in the most Effective, Efficient and Effortless way.<br>Never rely on translations again!</p>
    <div class="btn" style="left:514px;top:335px;width:172px;height:34px">Start Learning Now</div>
    <div class="arrow" style="left:23px"><svg width="10" height="12" viewBox="0 0 10 12"><path d="M8 1L3 6l5 5" fill="none" stroke="#111" stroke-width="2.5"/></svg></div>
    <div class="arrow" style="left:1144px"><svg width="10" height="12" viewBox="0 0 10 12"><path d="M2 1l5 5-5 5" fill="none" stroke="#111" stroke-width="2.5"/></svg></div>
  </section>

  <!-- about -->
  <h2 class="section-title" style="top:776px">About Us</h2>
  <div class="rule" style="left:585px;top:822px"></div>
  <p class="about-text" style="left:171px">Lorem Ipsum proin gravida nibh vel velit auctor aliquet. Aenean sollicitudin, lorem quis bibendum auctor, nisi elit consequat ipsum, nec sagittis sem nibh id elit. Duis sed odio sit amet nibh vulputate cursus a sit amet mauris. Morbi accumsan ipsum velit. Nam nec tellus a odio tincidunt auctor a ornare odio. Sed non mauris vitae erat consequat. Lorem Ipsum proin gravida nibh vel velit auctor aliquet. Aenean sollicitudin, lorem quis bibendum auctor, nisi elit consequat ipsum, nec sagittis sem nibh id elit. Duis sed.</p>
  <div class="abs about-mark"><i></i><b>QALAM</b></div>
  <p class="about-text" style="left:757px">Lorem Ipsum proin gravida nibh vel velit auctor aliquet. Aenean sollicitudin, lorem quis bibendum auctor, nisi elit consequat ipsum, nec sagittis sem nibh id elit. Duis sed odio sit amet nibh vulputate cursus a sit amet mauris. Morbi accumsan ipsum velit. Nam nec tellus a odio tincidunt auctor a ornare odio. Sed non mauris vitae erat consequat. Lorem Ipsum proin gravida nibh vel velit auctor aliquet. Aenean sollicitudin, lorem quis bibendum auctor, nisi elit consequat ipsum, nec sagittis sem nibh id elit. Duis sed.</p>

  <div class="card" style="left:31px;background:linear-gradient(180deg,#7a3a5a 0%,#3a1a2a 55%,#140a10 100%)" role="img" aria-label="Open book on an ornate golden stand">
    <h3>Course Title</h3><p>Duis sed odio sit amet nibh vulputate cursus a sit amet mauris. Morbi accumsan ipsum velit. Nam nec tellus.</p>
  </div>
  <div class="card" style="left:418px;background:linear-gradient(180deg,#9a7458 0%,#4a3020 55%,#150c08 100%)" role="img" aria-label="Hands holding prayer beads">
    <h3>Course Title</h3><p>Duis sed odio sit amet nibh vulputate cursus a sit amet mauris. Morbi accumsan ipsum velit. Nam nec tellus.</p>
  </div>
  <div class="card" style="left:806px;background:linear-gradient(180deg,#7f94a8 0%,#3b4a5a 55%,#10161e 100%)" role="img" aria-label="Two readers seen from behind on a patterned carpet">
    <h3>Course Title</h3><p>Duis sed odio sit amet nibh vulputate cursus a sit amet mauris. Morbi accumsan ipsum velit. Nam nec tellus.</p>
  </div>
  <div class="btn" style="left:536px;top:1419px;width:127px;height:37px">View All</div>

  <!-- video -->
  <div class="abs video" role="img" aria-label="Close-up of an open Arabic manuscript, video preview">
    <svg class="abs" style="left:395px;top:125px" width="88" height="88" viewBox="0 0 88 88"><circle cx="44" cy="44" r="41" fill="none" stroke="#fff" stroke-width="4"/><path d="M35 27l26 17-26 17z" fill="#fff"/></svg>
  </div>

  <!-- testimonial -->
  <h2 class="section-title" style="top:1868px">Client Says About Us</h2>
  <div class="rule" style="left:585px;top:1916px"></div>
  <p class="abs quote">Lorem ipsum dolor sit amet, consectetur adipisicing elit, sed do eiusmod tempor incididunt ut labore et dolore<br>magna aliqua. Ut enim ad minim veniam, quis nostrud exercitation ullamco laboris nisi ut aliquip ex ea<br>commodo consequat. Duis aute irure dolor in reprehenderit.</p>
  <div class="abs" style="left:0;top:2027px;width:1200px;text-align:center;font-size:12.5px;font-weight:700">YUSUF KARIM</div>
  <div class="abs" style="left:0;top:2048px;width:1200px;text-align:center;font-size:10px;font-style:italic">Student</div>
  <div class="abs dots"><span></span><span class="on"></span><span></span></div>

  <!-- why choose us -->
  <section class="abs why" role="img" aria-label="White mosque with a turquoise dome under a winter sky">
    <svg class="abs" style="left:0;top:0" width="1200" height="565"><circle cx="800" cy="150" r="365" fill="#0b2f55" opacity=".93"/></svg>
    <h2>Why Choose Us?</h2>
    <div class="abs" style="left:662px;top:167px;width:30px;height:3px;background:#fff"></div>
    <p style="top:190px">Lorem ipsum dolor sit amet, consectetur adipisicing elit, sed do eiusmod tempor incididunt ut labore et dolore magna aliqua. Ut enim ad minim veniam, quis nostrud exercitation ullamco laboris nisi ut aliquip ex ea commodo consequat. Duis aute irure dolor in reprehenderit in voluptate velit esse cillum dolore eu fugiat nulla pariatur. Excepteur sint occaecat.</p>
    <p style="top:318px">cupidatat non proident, sunt in culpa qui officia deserunt mollit anim id est laborum. Sed ut perspiciatis unde omnis iste natus error sit voluptatem accusantium.</p>
    <div class="btn-white">READ MORE</div>
  </section>

  <!-- contact -->
  <section class="contact">
    <div class="abs" style="left:52px;top:2756px;width:310px;height:350px;background:linear-gradient(135deg,#eef5fa,#f7fafc);border-radius:6px"></div>
    <h2>Contact Us</h2>
    <div class="rule" style="left:245px;top:2834px"></div>
    <div class="abs" style="left:245px;top:2860px;font-size:12.5px;color:#555">NEED HELP? CALL US</div>
    <div class="abs" style="left:244px;top:2895px;font-size:38px;font-weight:700;color:var(--blue)">+(555) 20-1339</div>
    <div class="abs" style="left:245px;top:2960px;font-size:12.5px;color:#777">Abc Ave 123 Street Example City KSA.</div>
    <div class="abs" style="left:245px;top:2998px;font-size:13px;font-weight:600;color:var(--blue)">info@example.com</div>

    <div class="field" style="top:2780px;height:36px">Name</div>
    <div class="field" style="top:2830px;height:36px">Email</div>
    <div class="field" style="top:2882px;height:113px">Message</div>
    <svg class="abs" style="left:926px;top:2791px" width="14" height="14" viewBox="0 0 24 24"><circle cx="12" cy="7" r="5" fill="#666"/><path d="M2 23c0-6 4-9 10-9s10 3 10 9z" fill="#666"/></svg>
    <svg class="abs" style="left:926px;top:2842px" width="15" height="12" viewBox="0 0 24 18"><rect width="24" height="18" rx="2" fill="#666"/><path d="M1 2l11 8 11-8" fill="none" stroke="#fff" stroke-width="2"/></svg>
    <svg class="abs" style="left:926px;top:2893px" width="16" height="14" viewBox="0 0 24 20"><ellipse cx="12" cy="9" rx="11" ry="8" fill="#666"/><path d="M4 14l-2 6 7-3z" fill="#666"/></svg>
    <div class="btn" style="left:612px;top:3015px;width:343px;height:37px;font-size:12px">Submit</div>
  </section>

  <!-- footer -->
  <footer class="abs footer" role="img" aria-label="Mosque domes at night">
    <div class="brand" style="left:172px;top:120px;font-size:28px;color:#fff"><i style="width:26px;height:26px;background:var(--teal)"></i>QALAM</div>
    <div class="abs fcol" style="left:392px;top:76px"><h4>SITE MAP</h4><ul><li>› Home</li><li>› About Us</li><li>› Courses</li><li>› FAQ's</li><li>› Contact Us</li></ul></div>
    <div class="abs fcol" style="left:612px;top:76px"><h4>USEFUL LINKS</h4><ul><li>› Terms &amp; Conditions</li><li>› Blogs</li><li>› Privacy Policy</li><li>› Testimonials</li><li>› Partners</li></ul></div>
    <div class="abs fcol" style="left:832px;top:76px"><h4>CONTACT US</h4><ul><li>● 1234 Street Name, City,</li><li>&nbsp;&nbsp;&nbsp;&nbsp;Example Country</li><li>✆ (555) 418-2276</li><li>✉ info@example.com</li></ul>
      <div class="social" style="margin-top:6px"><span></span><span></span><span></span><span></span></div></div>
  </footer>
  <div class="abs subscribe">
    <div class="abs" style="left:75px;top:16px;font-size:21px;font-weight:700;color:var(--blue);line-height:22px">SUBSCRIBE</div>
    <div class="abs" style="left:75px;top:40px;font-size:12.5px;font-weight:600;color:#333">OUR NEWSLETTER</div>
    <div class="abs" style="left:312px;top:24px;width:236px;height:28px;border:1px solid var(--line);border-radius:4px;font-size:10px;font-style:italic;color:#999;padding:8px 16px">Your Email Address*</div>
    <div class="btn" style="left:573px;top:24px;width:84px;height:28px;font-size:11.5px">Send</div>
  </div>
  <div class="abs bottombar">Copyright © QALAM 2020 | All Rights Reserved.</div>

</div>
</body>
</html>
```